Website design for commercial and residential security company

we're looking to see some new designs for an established company with no website.

homepage and one inner page

here is a link to the homepage content, sitemap, logo and more.
https://files.brontavel.net/share/7QxmPzLrTw2vNkdJhYcsa9eFgbUoiVwRn?view=open

call to action should be Request A Quote

if you have any questions please send them to us asap

thank you

1 page

Sans Serif

```html
<!DOCTYPE html>
<html lang="en">
<head>
<meta charset="utf-8">
<title>Keystone Watch Business Solutions</title>
<link href="https://fonts.googleapis.com/css2?family=Oswald:wght@400;500;600;700&family=Roboto:wght@400;500;700&display=swap" rel="stylesheet">
<style>
:root{
  --gold:#cba72f;
  --gold-dark:#b8951f;
  --ink:#1f1f1f;
  --text:#333333;
  --muted:#666666;
  --light:#f3f3f3;
  --white:#ffffff;
  --footer:#262626;
  --bar:#222222;
}
*{box-sizing:border-box;margin:0;padding:0}
html,body{width:1200px;height:3321px;overflow:hidden}
body{font-family:'Roboto',sans-serif;color:var(--text);background:var(--white);position:relative}
.heading{font-family:'Oswald',sans-serif;font-weight:500;text-transform:uppercase;color:var(--ink)}
.heading .accent{color:var(--gold)}

/* top bar */
.topbar{position:absolute;left:0;top:0;width:1200px;height:41px;background:var(--gold);color:var(--white);font-size:13px}
.topbar .item{position:absolute;top:13px;display:flex;align-items:center;gap:10px;white-space:nowrap}

/* header */
.site-header{position:absolute;top:41px;left:0;width:1200px;height:92px;background:var(--white)}
.brand{position:absolute;display:flex;align-items:center;gap:10px;font-family:'Oswald',sans-serif;font-weight:600;text-transform:uppercase;letter-spacing:.5px}
.brand .dot{width:18px;height:18px;border-radius:50%;background:var(--gold)}
.brand .name{line-height:1}
.brand .name small{display:block;font-size:10px;letter-spacing:2px;margin-top:4px}
.nav{position:absolute;left:460px;top:46px;display:flex;gap:21px;font-size:13px;font-weight:500;color:var(--ink)}
.nav .active{color:var(--gold)}
.btn-quote{position:absolute;display:flex;align-items:center;justify-content:center;gap:14px;background:var(--gold);color:var(--white);font-family:'Oswald',sans-serif;font-weight:500;text-transform:uppercase;font-size:15px;letter-spacing:.3px}

/* hero */
.hero{position:absolute;top:133px;left:0;width:1200px;height:488px;
  background:
    radial-gradient(ellipse 260px 360px at 1090px 250px,rgba(210,210,215,.55),rgba(210,210,215,0) 70%),
    radial-gradient(ellipse 340px 260px at 200px 160px,rgba(120,140,170,.45),rgba(120,140,170,0) 70%),
    radial-gradient(ellipse 260px 160px at 720px 330px,rgba(190,150,90,.35),rgba(190,150,90,0) 70%),
    linear-gradient(90deg,#46536a 0%,#303b4b 30%,#22262d 55%,#2d2c2a 75%,#5c5851 100%)}
.hero h1{position:absolute;top:82px;left:0;width:1200px;text-align:center;font-family:'Oswald',sans-serif;font-weight:700;font-size:48px;color:var(--white);letter-spacing:.5px}
.hero p{position:absolute;top:152px;left:0;width:1200px;text-align:center;color:var(--white);font-size:14px;line-height:24px}
.hero-btn{position:absolute;top:229px;height:56px;display:flex;align-items:center;justify-content:center;gap:14px;font-family:'Oswald',sans-serif;font-weight:500;font-size:16px;color:var(--white);text-transform:uppercase}
.hero-btn.commercial{left:389px;width:196px;background:var(--gold)}
.hero-btn.residential{left:637px;width:187px;background:#8f8f8f}
.slide-arrow{position:absolute;width:36px;height:36px;border-radius:50%;background:rgba(255,255,255,.25);display:flex;align-items:center;justify-content:center}
.products{position:absolute;left:294px;top:496px;width:615px;height:214px;border-radius:18px;
  background:linear-gradient(90deg,#ecebe8 0%,#dcdcdc 22%,#f2f2f0 45%,#d7d7d7 65%,#5a5a5c 82%,#3d3d3f 100%);
  box-shadow:0 14px 24px rgba(0,0,0,.18)}

/* features */
.features-band{position:absolute;top:621px;left:0;width:1200px;height:303px;background:var(--light)}
.feature{position:absolute;top:757px;width:190px;margin-left:-95px;text-align:center}
.feature .circle{width:80px;height:80px;border-radius:50%;background:var(--gold);margin:0 auto;display:flex;align-items:center;justify-content:center;box-shadow:0 4px 8px rgba(0,0,0,.12)}
.feature .label{margin-top:28px;font-size:12.5px;font-weight:500;color:var(--ink);text-transform:uppercase}
.feature-divider{position:absolute;top:754px;width:1px;height:142px;background:#e0e0e0}

/* welcome */
.welcome h2{position:absolute;left:155px;top:1012px;font-size:27px;line-height:38px}
.welcome .lead{position:absolute;left:156px;top:1100px;width:430px;font-size:14px;font-weight:500;line-height:24px;color:var(--ink)}
.welcome .body{position:absolute;left:156px;top:1166px;width:430px;font-size:12.5px;line-height:24px;color:var(--text)}
.btn-read{position:absolute;left:157px;top:1281px;width:147px;height:43px;background:var(--gold);color:var(--white);font-family:'Oswald',sans-serif;font-weight:500;font-size:15px;display:flex;align-items:center;justify-content:center;gap:16px}
.photo{position:absolute}

/* services */
.services{position:absolute;top:1402px;left:0;width:1200px;height:493px;background:var(--gold)}
.section-title{position:absolute;left:0;width:1200px;text-align:center;font-size:26px}
.service-card{position:absolute;top:113px;width:278px;height:319px;background:var(--white)}
.service-card .thumb{height:179px}
.service-card .icon{position:absolute;left:16px;top:202px}
.service-card h3{position:absolute;left:102px;top:204px;font-size:14px;font-weight:500;color:var(--ink)}
.service-card p{position:absolute;left:102px;top:229px;width:165px;font-size:11.5px;line-height:19px;color:var(--muted)}
.service-card .more{position:absolute;left:102px;top:287px;font-size:11px;font-weight:500;color:var(--gold);display:flex;align-items:center;gap:8px}
.round-arrow{position:absolute;top:236px;width:26px;height:26px;border-radius:50%;background:var(--white);display:flex;align-items:center;justify-content:center}

/* intro */
.intro{position:absolute;top:2526px;left:0;width:1200px;height:454px;background:#f4f3f1}
.intro .family{position:absolute;left:0;top:0;width:640px;height:454px;
  background:
    radial-gradient(ellipse 120px 150px at 520px 110px,rgba(140,120,200,.55),rgba(140,120,200,0) 70%),
    radial-gradient(ellipse 140px 170px at 340px 300px,rgba(40,90,190,.55),rgba(40,90,190,0) 70%),
    radial-gradient(ellipse 200px 200px at 170px 330px,rgba(120,140,170,.6),rgba(120,140,170,0) 70%),
    linear-gradient(90deg,#d9cfc2 0%,#c9b8a2 35%,#d8d2cc 65%,rgba(244,243,241,0) 100%)}
.intro h2{position:absolute;left:629px;top:48px;font-size:26px;line-height:38px}
.intro .desc{position:absolute;left:630px;top:140px;width:380px;font-size:12px;line-height:19px;color:var(--muted)}
.field{position:absolute;width:196px;height:49px;background:var(--white);border:1px solid #dddddd;font-size:12px;color:#999;padding:17px 0 0 22px}

/* contact bar */
.contact-bar{position:absolute;top:2980px;left:0;width:1200px;height:90px;background:var(--bar);color:var(--white);font-size:13px;border-bottom:1px solid #3a3a3a}
.contact-bar .item{position:absolute;top:38px;display:flex;align-items:center;gap:12px;white-space:nowrap}
.contact-bar b{font-weight:500}
.contact-bar .divider{position:absolute;top:0;width:1px;height:90px;background:#444}
.contact-bar .pip{position:absolute;top:86px;width:6px;height:6px;border-radius:50%;background:var(--gold)}

/* footer */
.footer{position:absolute;top:3070px;left:0;width:1200px;height:207px;background:var(--footer);color:#cfcfcf;font-size:12px}
.footer h4{position:absolute;font-size:12px;font-weight:500;color:var(--gold);text-transform:uppercase}
.footer ul{position:absolute;list-style:none;line-height:24px}
.social{position:absolute;top:93px;left:812px;display:flex;gap:15px}
.social span{width:28px;height:28px;border-radius:50%;background:#5a5a5a;display:block}
.copyright{position:absolute;top:3277px;left:0;width:1200px;height:44px;background:var(--gold);color:var(--white);font-size:11px;text-align:center;line-height:44px}
.copyright b{font-weight:500}
</style>
</head>
<body>

<div class="topbar">
  <div class="item" style="left:640px">
    <svg width="18" height="13" viewBox="0 0 18 13" fill="none" stroke="#fff" stroke-width="1.2"><rect x=".6" y=".6" width="16.8" height="11.8"/><path d="M.6 .6 9 7l8.4-6.4"/></svg>
    hello@keystonewatch-example.com
  </div>
  <div class="item" style="left:915px">
    <svg width="16" height="16" viewBox="0 0 24 24" fill="none" stroke="#fff" stroke-width="1.5"><path d="M5 3h4l2 5-2.5 1.5a11 11 0 0 0 6 6L16 13l5 2v4a2 2 0 0 1-2 2A16 16 0 0 1 3 5a2 2 0 0 1 2-2z"/></svg>
    (555) 014-2297
  </div>
</div>

<header class="site-header">
  <div class="brand" style="left:152px;top:24px;color:var(--ink);font-size:24px">
    <span class="dot"></span>
    <span class="name">Keystone Watch<small>Business Solutions</small></span>
  </div>
  <nav class="nav">
    <span class="active">Home</span><span>About us</span><span>Solutions</span><span>Resources</span><span>Contact</span>
  </nav>
  <div class="btn-quote" style="left:846px;top:27px;width:196px;height:45px">
    <svg width="26" height="22" viewBox="0 0 26 22" fill="none" stroke="#fff" stroke-width="1.3"><rect x="1" y="5" width="16" height="12"/><path d="M5 17v4l4-4"/><path d="M8 5V1h17v12h-8"/></svg>
    Request a quote
  </div>
</header>

<section class="hero" role="img" aria-label="Security camera mounted on a building and a hand holding a smart home phone app">
  <h1>PROTECT YOUR BUSINESS &amp; HOME NOW</h1>
  <p>We provide the best latest technology of equipment and our<br>staff are available in 24/7 at clients call.</p>
  <div class="hero-btn commercial">
    <svg width="24" height="26" viewBox="0 0 24 26" fill="none" stroke="#fff" stroke-width="1.3"><rect x="2" y="2" width="12" height="23"/><rect x="14" y="10" width="8" height="15"/><path d="M5 6h2M9 6h2M5 10h2M9 10h2M5 14h2M9 14h2M5 18h2M9 18h2"/></svg>
    Commercial
  </div>
  <div class="hero-btn residential">
    <svg width="28" height="26" viewBox="0 0 28 26" fill="none" stroke="#fff" stroke-width="1.3"><path d="M2 12 14 2l12 10"/><path d="M5 10v15h18V10"/><rect x="11" y="16" width="6" height="9"/></svg>
    Residential
  </div>
  <div class="slide-arrow" style="left:103px;top:219px"><svg width="10" height="14" viewBox="0 0 10 14" fill="none" stroke="#fff" stroke-width="1.5"><path d="M7 1 1 7l6 6"/></svg></div>
  <div class="slide-arrow" style="left:1062px;top:219px"><svg width="10" height="14" viewBox="0 0 10 14" fill="none" stroke="#fff" stroke-width="1.5"><path d="m3 1 6 6-6 6"/></svg></div>
</section>

<div class="features-band"></div>
<div class="products" role="img" aria-label="Security equipment: motion sensors, key fob, alarm keypad and dome cameras"></div>

<div class="feature" style="left:231px"><div class="circle"><svg width="30" height="38" viewBox="0 0 30 38" fill="none" stroke="#fff" stroke-width="1.5"><rect x="5" y="2" width="20" height="34" rx="2"/><circle cx="15" cy="10" r="4"/><path d="M10 20h10M10 25h10M10 30h10"/></svg></div><div class="label">Itercon Systems</div></div>
<div class="feature-divider" style="left:329px"></div>
<div class="feature" style="left:425px"><div class="circle"><svg width="40" height="36" viewBox="0 0 40 36" fill="none" stroke="#fff" stroke-width="1.5"><path d="M8 6 34 14l-3 8L5 14z"/><path d="M18 18l-3 8H6M6 20v12"/></svg></div><div class="label">CCTV</div></div>
<div class="feature-divider" style="left:513px"></div>
<div class="feature" style="left:607px"><div class="circle"><svg width="40" height="30" viewBox="0 0 40 30" fill="none" stroke="#fff" stroke-width="1.5"><rect x="3" y="3" width="34" height="6"/><path d="M7 9a13 13 0 0 0 26 0"/><circle cx="20" cy="15" r="5"/></svg></div><div class="label">IP Camera Systems</div></div>
<div class="feature-divider" style="left:696px"></div>
<div class="feature" style="left:790px"><div class="circle"><svg width="34" height="40" viewBox="0 0 34 40" fill="none" stroke="#fff" stroke-width="1.5"><rect x="4" y="3" width="22" height="34"/><rect x="10" y="9" width="10" height="14"/><circle cx="24" cy="30" r="5"/></svg></div><div class="label">Access Conteol</div></div>
<div class="feature-divider" style="left:880px"></div>
<div class="feature" style="left:976px"><div class="circle"><svg width="38" height="38" viewBox="0 0 38 38" fill="none" stroke="#fff" stroke-width="1.5"><path d="M11 30V20a8 8 0 0 1 16 0v10"/><path d="M6 30h26v4H6zM19 3v5M7 8l3 3M31 8l-3 3"/></svg></div><div class="label">Alarm Signaling</div></div>

<section class="welcome">
  <h2 class="heading">Welcome to Keystone Watch<br><span class="accent">Business Solutions</span></h2>
  <p class="lead">Vestibulum commodo at dolor eu aliquam. In congue ornare augue eu scelerisque. Duis vestibulum, dolor sed facilisis laoreet.</p>
  <p class="body">Nunc pretium nibh non aliquam scelerisque. Integer porttitor dolor sit amet leo malesuada scelerisque. Sed sed tortor lobortis, dictum lacus sed, mollis enim. Aenean ullamcorper accumsan sem sit amet aliquam. Cras euismod mauris felis, eget bibendum nibh facilisis ac.</p>
  <div class="btn-read">READ MORE <svg width="8" height="12" viewBox="0 0 8 12" fill="none" stroke="#fff" stroke-width="1.5"><path d="m2 1 5 5-5 5"/></svg></div>
  <div class="photo" style="left:611px;top:971px;width:429px;height:187px;background:radial-gradient(ellipse 110px 120px at 300px 80px,rgba(110,80,60,.55),rgba(110,80,60,0) 70%),linear-gradient(90deg,#3f5e5a 0%,#8fa9a6 30%,#c9d6d8 55%,#e6ecef 100%)" role="img" aria-label="Woman using a wall-mounted security panel"></div>
  <div class="photo" style="left:612px;top:1181px;width:254px;height:169px;background:radial-gradient(ellipse 70px 70px at 190px 70px,#2b2b2b 0%,#6b6b6b 40%,rgba(230,230,230,0) 75%),linear-gradient(120deg,#5e3a24 0%,#a7714a 35%,#dcc3a6 60%,#ece8e3 100%)" role="img" aria-label="Dome security camera above a staircase"></div>
  <div class="photo" style="left:891px;top:1183px;width:152px;height:134px;background:radial-gradient(ellipse 45px 35px at 80px 85px,#dfe3ea 0%,#3a3a3a 60%,rgba(0,0,0,0) 72%),linear-gradient(180deg,#f2ede6 0%,#e5d9c8 55%,#c9a67c 100%)" role="img" aria-label="Tablet showing a smart home app on a table"></div>
</section>

<section class="services">
  <h2 class="heading section-title" style="top:42px">Our <span style="color:var(--white)">Services</span></h2>
  <div class="round-arrow" style="left:96px"><svg width="6" height="10" viewBox="0 0 6 10" fill="none" stroke="#999" stroke-width="1.3"><path d="M5 1 1 5l4 4"/></svg></div>
  <div class="round-arrow" style="left:1072px"><svg width="6" height="10" viewBox="0 0 6 10" fill="none" stroke="#999" stroke-width="1.3"><path d="m1 1 4 4-4 4"/></svg></div>

  <div class="service-card" style="left:156px">
    <div class="thumb" style="background:radial-gradient(ellipse 60px 70px at 225px 100px,#fafafa 0%,#d8d8d8 60%,rgba(216,216,216,0) 80%),radial-gradient(ellipse 80px 40px at 100px 110px,#3b4652 0%,#6d7681 60%,rgba(109,118,129,0) 85%),linear-gradient(90deg,#556270,#9ea6ae 50%,#e8e8e8)" role="img" aria-label="Phone showing camera feeds beside a home camera"></div>
    <svg class="icon" width="66" height="56" viewBox="0 0 66 56" fill="none" stroke="#cba72f" stroke-width="2"><path d="M14 8 62 20l-4 12L10 20z"/><path d="M30 26l-4 12H10M8 30v22"/></svg>
    <h3>Security Camera</h3>
    <p>Duis et aliquam orci. Vivamus augue quam, ...quam ivamus</p>
    <div class="more">READ MORE <svg width="14" height="8" viewBox="0 0 14 8" fill="none" stroke="#cba72f" stroke-width="1.2"><path d="M0 4h13M10 1l3 3-3 3"/></svg></div>
  </div>
  <div class="service-card" style="left:460px">
    <div class="thumb" style="background:radial-gradient(ellipse 90px 55px at 140px 80px,#ffffff 0%,#eeeae7 55%,rgba(238,234,231,0) 75%),linear-gradient(135deg,#e9533f 0%,#f39a86 45%,#e8715c 75%,#d94232 100%)" role="img" aria-label="Smoke detector surrounded by red smoke"></div>
    <svg class="icon" width="66" height="56" viewBox="0 0 66 56" fill="none" stroke="#cba72f" stroke-width="2"><path d="M22 44V28a11 11 0 0 1 22 0v16"/><path d="M16 44h34v6H16zM33 4v8M16 12l5 5M50 12l-5 5"/></svg>
    <h3>Fire Alarm Systems</h3>
    <p>Duis et aliquam orci. Vivamus augue quam, ...quam ivamus</p>
    <div class="more">READ MORE <svg width="14" height="8" viewBox="0 0 14 8" fill="none" stroke="#cba72f" stroke-width="1.2"><path d="M0 4h13M10 1l3 3-3 3"/></svg></div>
  </div>
  <div class="service-card" style="left:766px">
    <div class="thumb" style="background:radial-gradient(ellipse 50px 90px at 80px 120px,#2a2a2a 0%,#5a524a 50%,rgba(90,82,74,0) 80%),radial-gradient(ellipse 55px 70px at 200px 140px,#7f8a96 0%,rgba(127,138,150,0) 75%),linear-gradient(90deg,#e2ded9,#cfc8c0 50%,#ecebe8)" role="img" aria-label="Woman on the phone and child using a wall tablet"></div>
    <svg class="icon" width="66" height="56" viewBox="0 0 66 56" fill="none" stroke="#cba72f" stroke-width="2"><rect x="18" y="4" width="26" height="46"/><rect x="25" y="12" width="12" height="18"/><circle cx="42" cy="42" r="7"/></svg>
    <h3>Home Automation</h3>
    <p>Duis et aliquam orci. Vivamus augue quam, ...quam ivamus</p>
    <div class="more">READ MORE <svg width="14" height="8" viewBox="0 0 14 8" fill="none" stroke="#cba72f" stroke-width="1.2"><path d="M0 4h13M10 1l3 3-3 3"/></svg></div>
  </div>
</section>

<section class="gallery">
  <h2 class="heading section-title" style="top:1930px">Our <span class="accent">Gallery</span></h2>
  <div class="photo" style="left:156px;top:2008px;width:432px;height:199px;background:radial-gradient(ellipse 90px 60px at 320px 110px,#f4f4f4 0%,#bfc3c6 60%,rgba(191,195,198,0) 80%),radial-gradient(ellipse 90px 90px at 70px 110px,#8e2f22 0%,#4a3430 50%,rgba(74,52,48,0) 80%),linear-gradient(90deg,#7a6a5c,#c8d9e4 50%,#e6eef3)" role="img" aria-label="Technician drilling to install a security camera"></div>
  <div class="photo" style="left:615px;top:2008px;width:432px;height:199px;background:radial-gradient(ellipse 110px 60px at 210px 110px,#1e1e1e 0%,#3a3a3a 55%,rgba(58,58,58,0) 75%),radial-gradient(ellipse 70px 40px at 90px 30px,#f0f0f0 0%,rgba(240,240,240,0) 80%),linear-gradient(90deg,#cfcfcf,#9c9c9c 50%,#d9c9bb)" role="img" aria-label="Hand holding a phone showing camera views under a dome camera"></div>
  <div class="photo" style="left:156px;top:2249px;width:278px;height:199px;background:radial-gradient(ellipse 40px 35px at 220px 70px,#7b72b8 0%,rgba(123,114,184,0) 80%),radial-gradient(ellipse 50px 80px at 120px 110px,#f7f7f7 0%,rgba(247,247,247,0) 80%),linear-gradient(90deg,#b8ab8f,#d7d4cc 45%,#c8ccb9)" role="img" aria-label="Wall intercom handset and video screen"></div>
  <div class="photo" style="left:461px;top:2249px;width:279px;height:199px;background:radial-gradient(circle at 60px 100px,#202020 0 26px,#f2f2f2 27px 52px,rgba(242,242,242,0) 60px),radial-gradient(circle at 190px 75px,#2a2a2a 0 20px,#eeeeee 21px 42px,rgba(238,238,238,0) 50px),linear-gradient(90deg,#cfcfcf,#b3b3b3 50%,#e3e3e3)" role="img" aria-label="Two white home security cameras"></div>
  <div class="photo" style="left:764px;top:2249px;width:279px;height:199px;background:radial-gradient(ellipse 50px 90px at 80px 130px,#2a2a2a 0%,#5a524a 50%,rgba(90,82,74,0) 80%),radial-gradient(ellipse 55px 70px at 200px 150px,#7f8a96 0%,rgba(127,138,150,0) 75%),linear-gradient(90deg,#e2ded9,#cfc8c0 50%,#ecebe8)" role="img" aria-label="Woman on the phone and child using a wall tablet"></div>
</section>

<section class="intro">
  <div class="family" role="img" aria-label="Father and son using a wall-mounted smart home panel"></div>
  <h2 class="heading">Introducing the most<br><span class="accent">Easiest security systems</span></h2>
  <p class="desc">Aorem ipsum dolor sit amet consectetur adipisicing anim elit dolore magna aliqua veniam quis nostrud.</p>
  <div class="field" style="left:626px;top:209px">Name</div>
  <div class="field" style="left:847px;top:209px">Email Address</div>
  <div class="field" style="left:626px;top:277px">Phone Number</div>
  <div class="field" style="left:847px;top:277px">Message</div>
  <div class="btn-quote" style="left:629px;top:357px;width:193px;height:53px">
    <svg width="30" height="24" viewBox="0 0 26 22" fill="none" stroke="#fff" stroke-width="1.3"><rect x="1" y="5" width="16" height="12"/><path d="M5 17v4l4-4"/><path d="M8 5V1h17v12h-8"/></svg>
    Request a quote
  </div>
</section>

<div class="contact-bar">
  <div class="item" style="left:165px">
    <svg width="18" height="18" viewBox="0 0 24 24" fill="none" stroke="#cba72f" stroke-width="1.5"><path d="M5 3h4l2 5-2.5 1.5a11 11 0 0 0 6 6L16 13l5 2v4a2 2 0 0 1-2 2A16 16 0 0 1 3 5a2 2 0 0 1 2-2z"/></svg>
    <span><b>Contact Us Free</b>&nbsp; (555) 014-2297</span>
  </div>
  <div class="divider" style="left:437px"></div><div class="pip" style="left:434px"></div>
  <div class="item" style="left:477px">
    <svg width="16" height="20" viewBox="0 0 16 20" fill="none" stroke="#cba72f" stroke-width="1.5"><path d="M8 19s7-7 7-11A7 7 0 0 0 1 8c0 4 7 11 7 11z"/><circle cx="8" cy="8" r="2.5"/></svg>
    <span><b>Office Address</b>&nbsp; 48 Harbor Lane Eastfield</span>
  </div>
  <div class="divider" style="left:764px"></div><div class="pip" style="left:761px"></div>
  <div class="item" style="left:790px">
    <svg width="18" height="13" viewBox="0 0 18 13" fill="none" stroke="#cba72f" stroke-width="1.2"><rect x=".6" y=".6" width="16.8" height="11.8"/><path d="M.6 .6 9 7l8.4-6.4"/></svg>
    <span><b>Email</b>&nbsp; hello@keystonewatch-example.com</span>
  </div>
</div>

<footer class="footer">
  <div class="brand" style="left:152px;top:48px;color:var(--white);font-size:24px">
    <span class="dot"></span>
    <span class="name">Keystone Watch<small>Business Solutions</small></span>
  </div>
  <h4 style="left:449px;top:55px">Quick Links</h4>
  <ul style="left:449px;top:82px"><li>Burglar Alarms</li><li>Home Security</li><li>Business Security</li></ul>
  <ul style="left:625px;top:81px"><li>Wireless alarms</li><li>Monitered Alarms</li><li>Company background</li></ul>
  <h4 style="left:809px;top:55px">Social Links</h4>
  <div class="social" aria-label="Social links"><span></span><span></span><span></span><span></span></div>
</footer>

<div class="copyright">Copyright © 2021. All rights reserved by, <b>KEYSTONE WATCH</b></div>

</body>
</html>
```